Lone Star Wetland Flora Stewardship Guild

We need to design the home page of this new website. We would like a fun website design for provides as a resource for members and information for potential members.
Please design so that we can see a portion of background on each side on the website.
I just need the final design files psd no coding needed.
Attached is their logo (colors are not 100% set in stone either so can mess with those as I did in the quick mockup attached)
Attached is a pdf newsletter they send out, you can get a feel for them and what they are about. The design is crappy and we are here to fix that going forward and we are starting with the website.
Here are some quick example websites (design style is open)
- I attached a quick mockup i did just for a content visual but by all means do what you want.
- http://www.brindlecourtleaders.org/
- http://www.qvelto.org/
- http://preview.plimworks7.com/view.php?cat=layoutpacks&host=gridcrafthub&temp=venrolite
- http://www.ploughvale.org/
- http://www.townmarrow.org/
- http://www.projectkindlecoat.org/
here are some of the other chapters website (pretty bad!)
and here are some of the others:
- http://www.zrelkq.org/
- http://ovtu.org/
- http://www.lirvx.org/
Content Items that need to be included:
1. Logo
2. Menu - home, about, members, resources, events, membership, contact
3. Become a member - button or action
4. social links - friendwall, jobrungo, clipzora
5. banner - that needs to explain their purpose "Promoting environmental stewardship through operations, research, education and outreach" (or this can be worked into the design)
6. Upcoming event (s)
7. Advertisement - members can place an ad on the website, this can be a placeholder for now
8. newsletter signup
9. advertise with us - this link can be in the footer
30-60 years of age, succesfull (household budgets of 120K+ men and women that live in texas.
Education

```html
<!DOCTYPE html>
<html lang="en">
<head>
<meta charset="utf-8">
<title>Lone Star Wetland Flora Stewardship Guild</title>
<link href="https://fonts.googleapis.com/css2?family=Open+Sans:wght@300;400;600&display=swap" rel="stylesheet">
<style>
:root{
  --red:#d5434f;
  --red-dark:#c1262f;
  --ink:#333;
  --muted:#777;
  --nav-bg:#f2f2f2;
  --rule:#e3c2c5;
  --footer-bg:#f4f4f4;
  --bottom:#393a3f;
  --white:#fff;
}
*{box-sizing:border-box;margin:0;padding:0}
html,body{width:828px;height:1200px;overflow:hidden;background:var(--white)}
body{position:relative;font-family:"Open Sans",Arial,sans-serif;color:var(--ink)}
.abs{position:absolute}

/* header */
.brand{left:48px;top:32px;display:flex;align-items:center;gap:8px}
.brand-dot{width:26px;height:26px;border-radius:50%;background:var(--red)}
.brand-name{font-size:12px;font-weight:600;color:var(--red-dark);line-height:1.25;width:140px}
.util{top:11px;left:602px;display:flex;gap:14px;font-size:9.5px;color:var(--muted);align-items:center}
.util span{display:flex;align-items:center;gap:4px}
.util .sep{width:1px;height:12px;background:#ccc}
.join{left:602px;top:70px;width:185px;height:28px;background:var(--red);color:var(--white);font-size:11px;font-weight:300;padding:7px 0 0 14px;letter-spacing:.2px}
.join b{font-weight:600}
.join-icon{left:732px;top:42px}

/* nav */
.nav{left:0;top:109px;width:828px;height:46px;background:var(--nav-bg);border-bottom:4px solid var(--red);box-sizing:content-box}
.nav a{position:absolute;top:0;height:46px;line-height:46px;text-align:center;font-size:10.5px;color:#333;text-decoration:none;border-right:1px solid #e2e2e2}
.nav a.on{background:var(--red);color:var(--white);border:0}

/* hero */
.hero{left:0;top:159px;width:828px;height:389px;background:linear-gradient(180deg,#e9eef2 0%,#dfe9ef 28%,#7fa24d 40%,#5d7f36 50%,#8fa7b3 56%,#6f8f99 68%,#a7b46a 82%,#95a455 100%)}
.arrow{top:312px;width:44px;height:44px;background:var(--white);display:flex;align-items:center;justify-content:center}
.caption{left:0;top:410px;width:426px;height:58px;background:rgba(255,255,255,.85);border-bottom:4px solid var(--red);clip-path:polygon(0 0,95% 0,100% 100%,0 100%);padding:10px 0 0 15px;font-size:13px;font-weight:300;line-height:16px;color:#222}

/* content */
.h2{font-size:15.5px;font-weight:300;color:#222}
.h2-rule{height:1px;background:var(--rule)}
.about-text{left:29px;top:622px;width:211px;font-size:9.1px;line-height:13.8px;color:#555;text-align:justify}
.about-text p+p{margin-top:13.8px}
.event{left:304px;width:233px;display:flex;gap:15px}
.thumb{width:57px;height:44px;border:3px solid var(--white);box-shadow:0 0 2px rgba(0,0,0,.35);flex:none}
.event-text{font-size:9.1px;line-height:12.5px;color:#666;padding-top:4px}
.event-text .hl{color:var(--red-dark)}
.ev-rule{left:304px;width:233px;height:1px;background:#e6e6e6}
.more{top:820px;width:57px;height:23px;background:var(--red);border-bottom:3px solid var(--red-dark);color:var(--white);font-size:10.5px;text-align:center;line-height:21px}
.ad{left:602px;top:589px;width:199px;height:256px;background:linear-gradient(180deg,#7fb1d6 0%,#3d6f98 45%,#2c3e56 78%,#d6d6d6 79%,#e4e4e4 100%)}

/* newsletter */
.news{left:0;top:885px;width:803px;height:58px;background:var(--red)}
.news-lead{left:0;top:885px;width:302px;height:58px;background:var(--red-dark);clip-path:polygon(0 0,95% 0,100% 50%,95% 100%,0 100%);color:var(--white);font-size:13px;font-weight:300;padding:19px 0 0 43px}
.email{left:335px;top:903px;width:331px;height:22px;background:var(--white);border:1px solid #bbb;font-size:7.5px;color:#777;padding:6px 0 0 6px}
.submit{left:691px;top:903px;width:82px;height:22px;background:#2f2f33;border-bottom:2px solid #111;color:var(--white);font-size:10.5px;text-align:center;line-height:21px}

/* footer */
.footer{left:0;top:943px;width:828px;height:206px;background:var(--footer-bg)}
.f-h{top:977px;font-size:12.5px;font-weight:300;color:#333}
.f-rule{top:997px;height:1px;background:#ddd}
.f-rule i{display:block;height:2px;background:var(--red);margin-top:-1px}
.f-list{top:1014px;font-size:8px;line-height:14.5px;color:#888;list-style:none}
.f-list .on{color:var(--red)}
.social li{display:flex;align-items:center;gap:6px;line-height:19.5px}
.social .ico{width:12px;height:12px;border-radius:50%;background:#444}
.adv{left:231px;top:1083px;background:var(--red-dark);color:var(--white);font-size:9px;padding:2px 7px 3px;border-radius:2px}
.bottom{left:0;top:1149px;width:828px;height:51px;background:var(--bottom);color:#888;font-size:8.5px;text-align:center;line-height:51px}
</style>
</head>
<body>

<!-- header -->
<div class="abs brand">
  <div class="brand-dot"></div>
  <div class="brand-name">Lone Star Wetland Flora Stewardship Guild</div>
</div>
<div class="abs util">
  <span><svg width="9" height="11" viewBox="0 0 9 11"><rect x="0.5" y="4.5" width="8" height="6" fill="#777"/><path d="M2 4.5V3a2.5 2.5 0 0 1 5 0v1.5" stroke="#777" fill="none"/></svg>LOGIN</span>
  <i class="sep"></i>
  <span><svg width="11" height="11" viewBox="0 0 11 11"><circle cx="5.5" cy="5.5" r="5" stroke="#777" fill="none"/><path d="M3.5 3.2l1 -.2.8 1.6-.7.6a4 4 0 0 0 1.6 1.6l.6-.7 1.6.8-.2 1c-2.6 0-4.8-2.1-4.7-4.7z" fill="#777"/></svg>CONTACT US</span>
</div>
<div class="abs join">BECOME A <b>MEMBER</b></div>
<svg class="abs join-icon" width="48" height="52" viewBox="0 0 48 52" aria-hidden="true">
  <circle cx="22" cy="13" r="11" fill="#222"/>
  <path d="M2 52c0-16 9-24 20-24s20 8 20 24z" fill="#222"/>
  <circle cx="37" cy="41" r="9" fill="#222" stroke="#fff" stroke-width="2"/>
  <path d="M37 36v10M32 41h10" stroke="#fff" stroke-width="2.2"/>
</svg>

<!-- nav -->
<nav class="abs nav">
  <a class="on" style="left:26px;width:90px">HOME</a>
  <a style="left:116px;width:97px">ABOUT</a>
  <a style="left:213px;width:102px">MEMBERS</a>
  <a style="left:315px;width:117px">RESOURCES</a>
  <a style="left:432px;width:110px">EVENTS</a>
  <a style="left:542px;width:129px">MEMBERSHIP</a>
  <a style="left:671px;width:110px;border:0">CONTACT</a>
</nav>

<!-- hero -->
<div class="abs hero" role="img" aria-label="Photo of a calm pond with floating lily pads, trees along the far bank under a pale sky"></div>
<div class="abs arrow" style="left:0"><svg width="12" height="22" viewBox="0 0 12 22"><path d="M11 1L1 11l10 10" stroke="#555" stroke-width="2" fill="none"/></svg></div>
<div class="abs arrow" style="left:784px"><svg width="12" height="22" viewBox="0 0 12 22"><path d="M1 1l10 10L1 21" stroke="#555" stroke-width="2" fill="none"/></svg></div>
<div class="abs caption">PROMOTING ENVIRONMENTAL STEWARDSHIP<br>THROUGH OPERATIONS, RESEARCH, EDUCATION AND OUTREACH</div>

<!-- about -->
<h2 class="abs h2" style="left:29px;top:576px">About&nbsp; LSWFSG</h2>
<div class="abs h2-rule" style="left:29px;top:600px;width:211px"></div>
<div class="abs about-text">
  <p>The Lone Star Wetland Flora Stewardship Guild, Inc. is an organization of scientists, educators, students, commercial pesticide applicators, administrators, and concerned individuals interested in the management and study of aquatic plants.</p>
  <p>The membership reflects a diversity of federal, state, and local agencies; universities and colleges around the world; corporations; and small businesses.</p>
</div>
<div class="abs more" style="left:31px">More</div>

<!-- events -->
<h2 class="abs h2" style="left:304px;top:576px">Upcoming Events</h2>
<div class="abs h2-rule" style="left:304px;top:600px;width:233px"></div>
<div class="abs event" style="top:623px">
  <div class="thumb" style="background:#eee" role="img" aria-label="Ranch lodge logo"></div>
  <div class="event-text">2014 LSWFSG CONFERENCE<br>OCTOBER 12-2014<br><span class="hl">MESQUITE BEND RANCH</span></div>
</div>
<div class="abs ev-rule" style="top:676px"></div>
<div class="abs event" style="top:686px">
  <div class="thumb" style="background:linear-gradient(180deg,#6f8a3e,#8a9a5a)" role="img" aria-label="Lily pads on a pond"></div>
  <div class="event-text">Lorem ipsum dolor sit amet, consectetur adipisicing elit, sed do eiusmod tempor incididunt ut labore et dolore</div>
</div>
<div class="abs ev-rule" style="top:744px"></div>
<div class="abs event" style="top:753px">
  <div class="thumb" style="background:linear-gradient(180deg,#5d7f36,#7f9b8f)" role="img" aria-label="Trees reflected in a pond"></div>
  <div class="event-text">Lorem ipsum dolor sit amet, consectetur adipisicing elit, sed do eiusmod tempor incididunt ut labore et dolore</div>
</div>
<div class="abs more" style="left:305px">More</div>

<!-- advertisement -->
<div class="abs ad" role="img" aria-label="Sponsor advertisement showing an aquatic algae treatment product"></div>

<!-- newsletter -->
<div class="abs news"></div>
<div class="abs news-lead">SUBSCRIBE TO OUR NEWSLETTER</div>
<div class="abs email">Enter your email :</div>
<div class="abs submit">SUBMIT</div>

<!-- footer -->
<div class="abs footer"></div>

<div class="abs f-h" style="left:43px">NAVIGATION</div>
<div class="abs f-rule" style="left:43px;width:116px"><i style="width:78px"></i></div>
<ul class="abs f-list" style="left:45px">
  <li class="on">HOME</li><li>ABOUT</li><li>MEMBERS</li><li>RESOURCES</li><li>EVENTS</li><li>MEMBERSHIP</li><li>CONTACT</li>
</ul>

<div class="abs f-h" style="left:232px">FOR MEMBERS</div>
<div class="abs f-rule" style="left:232px;width:124px"><i style="width:90px"></i></div>
<ul class="abs f-list" style="left:232px">
  <li>FORUMS</li><li>PROMOTIONS</li><li>SIGN IN</li><li>NEWS</li>
</ul>
<div class="abs adv">Advertise with us</div>

<div class="abs f-h" style="left:445px">FOLLOW US</div>
<div class="abs f-rule" style="left:445px;width:122px"><i style="width:74px"></i></div>
<ul class="abs f-list social" style="left:445px;top:1010px">
  <li><i class="ico"></i>FRIENDWALL</li><li><i class="ico"></i>JOBRUNGO</li><li><i class="ico"></i>CLIPZORA</li>
</ul>

<div class="abs f-h" style="left:632px">OUR LOCATION</div>
<div class="abs f-rule" style="left:632px;width:163px"><i style="width:96px"></i></div>
<ul class="abs f-list" style="left:635px;line-height:13px">
  <li>Lone Star Wetland Flora Stewardship</li><li>Guild Address</li><li>Attn: Reid Calloway, Treasurer</li><li>P.O. Box 481</li><li>Brenfield, Texas 79912</li><li>Email: rcalloway@wetflora.org</li>
</ul>

<div class="abs bottom">Copyright © 2014 | Privacy Policy, All Rights Reserved</div>

</body>
</html>
```